Tarnholt Bright Press Label

We are looking for a label for our blueberry vodka and lemonade ready-to-drink cocktail. we would like the ingredients (vodka, lemon juice, cane sugar, blueberries) discretely displayed on the label. We would also like 15% alc/vol (30 proof) on the label. The label is for a 12-ounce slim can. We would also like the Surgeon Generals warning ion the label

Target Market(s)

Spike seltzer and ready to drink cocktail drinkers

Font styles to use
Decorative

Requirements
Must have
• Surgeon General warning, 15% alc/vol (30 proof) 12 ounces., Ingredients

```html
<!DOCTYPE html>
<html lang="en">
<head>
<meta charset="utf-8">
<title>Tarnholt Bright Press – Blueberry Vodka Label</title>
<link rel="stylesheet" href="https://fonts.googleapis.com/css2?family=Cinzel+Decorative:wght@700&family=Roboto+Condensed:wght@400&family=Teko:wght@500&display=swap">
<style>
  :root {
    --backdrop: #c4cad3;
    --navy-top: #132b5e;
    --navy-bottom: #0e173a;
    --navy-ink: #14183a;
    --silver: #e2e4e8;
    --white: #ffffff;
    --berry-tone: #2a3f73;
  }
  * { margin: 0; padding: 0; box-sizing: border-box; }
  html, body {
    width: 1200px; height: 1200px; overflow: hidden;
    background: var(--backdrop);
  }
  .label {
    position: absolute; left: 365px; top: 39px;
    width: 470px; height: 1122px;
    background: var(--silver);
    overflow: hidden;
    box-shadow: 0 2px 6px rgba(0,0,0,0.18);
  }
  .label-top {
    position: absolute; left: 0; top: 0; width: 470px; height: 780px;
  }
  .tagline {
    position: absolute; left: 0; top: 50px; width: 470px; height: 110px;
    overflow: visible;
  }
  .tagline text {
    font-family: "Teko", sans-serif; font-weight: 500;
    font-size: 31px; fill: var(--white); letter-spacing: 0.5px;
  }
  .berry-art {
    position: absolute; left: 175px; top: 154px; width: 120px; height: 98px;
    background: radial-gradient(circle at 50% 60%, var(--berry-tone), rgba(42,63,115,0.25) 70%, transparent 72%);
  }
  .product-name {
    position: absolute; left: 0; top: 282px; width: 470px; text-align: center;
    font-family: "Cinzel Decorative", serif; font-weight: 700;
    font-size: 64px; line-height: 1; color: var(--white); letter-spacing: -1px;
  }
  .spirit-band {
    position: absolute; left: 98px; top: 381px; width: 294px; height: 74px;
    background: var(--white); border-radius: 14px 4px 4px 14px;
  }
  .spirit-name {
    position: absolute; left: 98px; top: 392px; width: 294px; text-align: center;
    font-family: "Cinzel Decorative", serif; font-weight: 700;
    font-size: 44px; line-height: 52px; color: var(--navy-ink);
  }
  .ingredients {
    position: absolute; left: 0; top: 560px; width: 470px; text-align: center;
    font-family: "Roboto Condensed", sans-serif; font-size: 20px; line-height: 25px;
    color: var(--white);
  }
  .strength {
    position: absolute; top: 635px; text-align: center;
    font-family: "Roboto Condensed", sans-serif; font-size: 20px; line-height: 25px;
    color: var(--white);
  }
  .strength--proof { left: 40px; width: 80px; }
  .strength--abv { right: 20px; width: 96px; }
  .warning {
    position: absolute; left: 14px; top: 1068px;
    width: 280px;
    transform: rotate(-90deg); transform-origin: 0 0;
    font-family: "Roboto Condensed", sans-serif; font-size: 8px; line-height: 10px;
    color: var(--navy-ink);
  }
  .volume {
    position: absolute; left: 0; top: 985px; width: 470px; text-align: center;
    color: var(--navy-ink);
  }
  .volume-oz {
    font-family: "Teko", sans-serif; font-weight: 500; font-size: 48px; line-height: 44px;
    letter-spacing: 1px;
  }
  .volume-ml {
    font-family: "Roboto Condensed", sans-serif; font-size: 18px; line-height: 22px;
  }
</style>
</head>
<body>
  <div class="label">
    <svg class="label-top" viewBox="0 0 470 780" aria-hidden="true">
      <defs>
        <linearGradient id="navyFill" x1="0" y1="0" x2="0" y2="1">
          <stop offset="0" stop-color="var(--navy-top)"/>
          <stop offset="1" stop-color="var(--navy-bottom)"/>
        </linearGradient>
      </defs>
      <path d="M0 0 H470 V728 C430 745 390 772 343 770 C270 766 200 705 118 707 C70 708 30 728 0 742 Z" fill="url(#navyFill)"/>
    </svg>

    <svg class="tagline" viewBox="0 0 470 110">
      <path id="taglineArc" d="M50 100 Q235 20 420 100" fill="none"/>
      <text><textPath href="#taglineArc" startOffset="50%" text-anchor="middle">READY-TO-DRINK COCKTAIL</textPath></text>
    </svg>

    <div class="berry-art" role="img" aria-label="Engraved sketch of three blueberries with leaves"></div>

    <h1 class="product-name">Blueberry</h1>
    <div class="spirit-band" role="img" aria-label="White brush stroke"></div>
    <p class="spirit-name">Vodka</p>

    <p class="ingredients">Vodka, Lemon Juice, Cane Sugar,<br>Blueberries</p>
    <p class="strength strength--proof">30<br>PROOF</p>
    <p class="strength strength--abv">15%<br>ALC/VOL</p>

    <p class="warning">GOVERNMENT WARNING: (1) According to the Surgeon General, women should not drink alcoholic beverages during pregnancy because of the risk of birth defects. (2) Consumption of alcoholic beverages impairs your ability to drive a car or operate machinery, and may cause health problems.</p>

    <div class="volume">
      <p class="volume-oz">12 FL OZ</p>
      <p class="volume-ml">(355 ML)</p>
    </div>
  </div>
</body>
</html>
```